letterhead design for a investing company*

Design an appealing business letterhead to match with our existing logo and attract new customers. Our customers are mainly corporate managers which are detail oriented and judge the company ability to perform a good service based on small details. A professional letterhead will give a good first impression.

Target Market(s)

New customers and business owners

Industry/Entity Type

Marketplace

Font styles to use
Sans Serif
Script

Requirements
Must have
• Must be a professional and elegant design that attracts interest from people who receives it

```html
<!DOCTYPE html>
<html lang="en">
<head>
<meta charset="utf-8">
<title>NorthKeel Letterhead</title>
<link rel="stylesheet" href="https://fonts.googleapis.com/css2?family=Open+Sans:wght@400&family=Roboto:wght@400;500;700&display=swap">
<style>
  :root {
    --navy: #121c3f;
    --gold: #f6b800;
    --paper: #ffffff;
    --backdrop: #e3e3e5;
    --body-text: #6b6b6b;
    --address-text: #3a3a3a;
    --ink: #1a1a1a;
  }
  * { box-sizing: border-box; margin: 0; padding: 0; }
  html, body {
    width: 1196px;
    height: 1200px;
    overflow: hidden;
    background: var(--backdrop);
  }
  .letterhead {
    position: absolute;
    left: 202px;
    top: 40px;
    width: 792px;
    height: 1120px;
    background: var(--paper);
    box-shadow: 0 6px 24px rgba(0,0,0,0.12);
  }
  .letterhead__header {
    height: 143px;
    background: var(--navy);
    border-bottom: 6px solid var(--gold);
    display: flex;
    align-items: center;
    justify-content: space-between;
    padding: 0 71px 0 71px;
  }
  .brand {
    display: flex;
    align-items: center;
    gap: 12px;
  }
  .brand__dot {
    width: 26px;
    height: 26px;
    border-radius: 50%;
    background: var(--gold);
  }
  .brand__name {
    font-family: 'Roboto', sans-serif;
    font-weight: 700;
    font-size: 36px;
    color: var(--paper);
    letter-spacing: 0.2px;
  }
  .contact {
    list-style: none;
    font-family: 'Roboto', sans-serif;
    font-size: 17px;
    line-height: 22px;
    color: var(--paper);
    margin-right: 0;
  }
  .contact__item {
    display: flex;
    align-items: center;
    gap: 6px;
  }
  .contact__icon {
    width: 13px;
    height: 13px;
    flex: none;
  }
  .letter {
    position: absolute;
    left: 73px;
    right: 71px;
    top: 263px;
    font-family: 'Open Sans', sans-serif;
    font-size: 14.6px;
    line-height: 21.6px;
    color: var(--body-text);
  }
  .letter p {
    margin-bottom: 21.6px;
    text-align: justify;
    hyphens: auto;
  }
  .signature {
    position: absolute;
    left: 73px;
    top: 1010px;
  }
  .signature-area {
    position: absolute;
    left: 75px;
    top: 820px;
    width: 92px;
    height: 92px;
    background: linear-gradient(135deg, #f2f2f2, #e4e4e4);
    border-radius: 4px;
  }
  .letterhead__footer {
    position: absolute;
    left: 0;
    right: 0;
    top: 1058px;
    text-align: center;
    font-family: 'Roboto', sans-serif;
    font-weight: 400;
    font-size: 20px;
    color: var(--address-text);
  }
</style>
</head>
<body>
  <main class="letterhead">
    <header class="letterhead__header">
      <div class="brand">
        <span class="brand__dot"></span>
        <span class="brand__name">NorthKeel</span>
      </div>
      <ul class="contact">
        <li class="contact__item">
          <svg class="contact__icon" viewBox="0 0 16 16"><path fill="#f6b800" d="M1 5c0-2 3-3 7-3s7 1 7 3v1h-3.5V4.5h-7V6H1z M3 7h10l2 7H1z M8 9a2 2 0 1 0 0 4a2 2 0 0 0 0-4z"/></svg>
          <span>555.204.7788</span>
        </li>
        <li class="contact__item">
          <svg class="contact__icon" viewBox="0 0 16 16"><rect x="1" y="3" width="14" height="10" fill="#f6b800"/><path d="M1 3l7 6 7-6" fill="none" stroke="#121c3f" stroke-width="1.4"/></svg>
          <span>hello@northkeel.com.au</span>
        </li>
        <li class="contact__item">
          <svg class="contact__icon" viewBox="0 0 16 16"><circle cx="8" cy="8" r="7" fill="#f6b800"/><path d="M1 8h14M8 1c-3 3-3 11 0 14M8 1c3 3 3 11 0 14" fill="none" stroke="#121c3f" stroke-width="1.1"/></svg>
          <span>www.northkeel.com.au</span>
        </li>
      </ul>
    </header>

    <article class="letter">
      <p>Dear customer,</p>
      <p>Lorem ipsum dolor sit amet, consectetur adipisicing elit, sed do eiusmod tempor incididunt ut labore et dolore magna aliqua. Ut enim ad minim veniam, quis nostrud exercitation ullamco laboris nisi ut aliquip ex ea commodo consequat. Duis aute irure dolor in reprehenderit in voluptate velit esse cillum dolore eu fugiat nulla pariatur. Excepteur sint occaecat cupidatat non proident, sunt in culpa qui officia deserunt mollit anim id est laborum.</p>
      <p>Lorem ipsum dolor sit amet, consectetur adipisicing elit, sed do eiusmod tempor incididunt ut labore et dolore magna aliqua. Ut enim ad minim veniam, quis nostrud exercitation ullamco laboris nisi ut aliquip ex ea commodo consequat. Duis aute irure dolor in reprehenderit in voluptate velit esse cillum dolore eu fugiat nulla pariatur. Excepteur sint occaecat cupidatat non proident, sunt in culpa qui officia deserunt mollit anim id est laborum.</p>
      <p>Lorem ipsum dolor sit amet, consectetur adipisicing elit, sed do eiusmod tempor incididunt ut labore et dolore magna aliqua. Ut enim ad minim veniam, quis nostrud exercitation ullamco laboris nisi ut aliquip ex ea commodo consequat. Duis aute irure dolor in reprehenderit in voluptate velit esse cillum dolore eu fugiat nulla pariatur. Excepteur sint occaecat cupidatat non proident, sunt in culpa qui officia deserunt mollit anim id est laborum.</p>
      <p>Lorem ipsum dolor sit amet, consectetur adipisicing elit, sed do eiusmod tempor incididunt ut labore et dolore magna aliqua. Ut enim ad minim veniam, quis nostrud exercitation ullamco laboris nisi ut aliquip ex ea commodo consequat. Duis aute irure dolor in reprehenderit.</p>
      <p>Yours Sincerely,</p>
    </article>

    <div class="signature-area" role="img" aria-label="Handwritten signature of the sender"></div>

    <footer class="letterhead__footer">48 Harbour Crest Road, Lakefield, ON K0L 1H0</footer>
  </main>
</body>
</html>
```